label for a bottle of Whiskey.

the winner will realize 4 other label in a different project.
We are looking for someone who can create a label for our Whiskey bottle. Our distillery is called Marden Hollow Still works. We want to stay with the American Revolutionary War era theme. We have a custom bottle with a statue of Elias Thornbury on top and a cannon front the sided have our name on an angle from top to bottom. I can provide pictures of the bottle for reference. We have 7 different whiskey's and want to use the same label just change out the name/type of Whiskey. We have a White Whiskey, Rye, sweet corn, cask strength, 4 grain , honey, cinnamon and bourbon.
We are competing in a market saturated with established products, I need your best work! If you can come up with a great label, I will give the winner 4 more label categories. We make moonshine, Rum, Vodka, Gin, Brandy.
All of these products were available and desired in colonial times. I feel strongly that whoever takes on this project will need to research other Whiskey brands and also Marden Hollow National park and the American Revolution!
We have two size bottles, 750 Ml and a small 50ml we would like a scaled down version for the 50ml, but our main bottle is 750 ml.

Target Market(s)

Whiskey drinkers

Colors

Designer to choose colors to be used in the design.

Requirements
Must have
• The theme of the colonial times, revolutionary war theme.
Nice to have
• I listed everything in the description. But the label cannot be too busy!
Should not have
• Allot of colors. I do like colors such as copper, pewter and the burnt , patina look.
• I am not a designer, I am depending on someone doing their research!

```html
<!DOCTYPE html>
<html lang="en">
<head>
<meta charset="utf-8">
<title>Marden Hollow Still Works – White Whiskey Label</title>
<link rel="stylesheet" href="https://fonts.googleapis.com/css2?family=UnifrakturMaguntia&family=Josefin+Sans:wght@400&family=Alfa+Slab+One&family=IM+Fell+English+SC&family=IM+Fell+English:ital@1&display=swap">
<style>
  :root {
    --backdrop: #303030;
    --paper: #efe5c6;
    --paper-edge: #e4d6ae;
    --copper: #ea7a2c;
    --copper-deep: #c9622a;
    --ink: #4a3f33;
    --engraving-dark: #6b6150;
    --engraving-light: #cfc4a6;
  }
  * { box-sizing: border-box; margin: 0; padding: 0; }
  html, body { width: 1200px; height: 1200px; overflow: hidden; background: var(--backdrop); }
  .board { position: relative; width: 1200px; height: 1200px; }

  .label {
    position: absolute;
    width: 512px;
    height: 496px;
    background: radial-gradient(ellipse at 40% 30%, var(--paper) 55%, var(--paper-edge) 100%);
    overflow: hidden;
  }
  .label--rounded { left: 345px; top: 69px; border-radius: 8px; }
  .label--deckle {
    left: 342px; top: 622px;
    clip-path: polygon(
      0 3px, 24px 0, 46px 4px, 70px 1px, 95px 5px, 118px 0, 142px 3px, 166px 0, 190px 4px, 214px 1px, 238px 5px, 262px 0, 286px 3px, 310px 1px, 334px 5px, 358px 0, 382px 3px, 406px 1px, 430px 4px, 454px 0, 478px 3px, 500px 1px, 512px 4px,
      508px 24px, 512px 48px, 507px 72px, 511px 96px, 508px 120px, 512px 144px, 507px 168px, 511px 192px, 508px 216px, 512px 240px, 507px 264px, 511px 288px, 508px 312px, 512px 336px, 507px 360px, 511px 384px, 508px 408px, 512px 432px, 507px 456px, 511px 480px, 508px 496px,
      488px 492px, 464px 496px, 440px 491px, 416px 495px, 392px 492px, 368px 496px, 344px 491px, 320px 495px, 296px 492px, 272px 496px, 248px 491px, 224px 495px, 200px 492px, 176px 496px, 152px 491px, 128px 495px, 104px 492px, 80px 496px, 56px 491px, 32px 495px, 8px 492px,
      4px 472px, 0 448px, 5px 424px, 1px 400px, 4px 376px, 0 352px, 5px 328px, 1px 304px, 4px 280px, 0 256px, 5px 232px, 1px 208px, 4px 184px, 0 160px, 5px 136px, 1px 112px, 4px 88px, 0 64px, 5px 40px, 1px 16px);
  }

  .brand-title {
    position: absolute; left: 0; right: 0; top: 26px;
    text-align: center;
    font-family: "UnifrakturMaguntia", serif;
    font-size: 66px; line-height: 1;
    font-weight: 400;
    transform: scaleY(1.45); transform-origin: top center;
    color: var(--copper);
    background: linear-gradient(90deg, var(--copper), var(--copper-deep));
    -webkit-background-clip: text; background-clip: text;
    -webkit-text-fill-color: transparent;
  }
  .brand-sub {
    position: absolute; left: 0; right: 0; top: 128px;
    text-align: center;
    font-family: "Josefin Sans", sans-serif;
    font-size: 30px; line-height: 1; letter-spacing: 1px;
    color: var(--copper);
  }
  .brand-sub .star { font-size: 14px; vertical-align: middle; margin: 0 6px; }

  .scene {
    position: absolute; left: 40px; top: 168px; width: 318px; height: 176px;
    background: linear-gradient(180deg, rgba(207,196,166,0) 0%, var(--engraving-light) 30%, var(--engraving-dark) 85%);
    border-radius: 40% 40% 6px 6px / 30% 30% 6px 6px;
    opacity: .85;
  }

  .maker-mark {
    position: absolute; left: 362px; top: 196px; width: 124px;
    display: flex; flex-direction: column; align-items: center; gap: 8px;
  }
  .maker-mark .dot { width: 80px; height: 80px; border-radius: 50%; background: var(--copper); }
  .maker-mark .name {
    font-family: "Josefin Sans", sans-serif; font-size: 13px;
    color: var(--copper-deep); text-align: center; line-height: 1.2;
  }

  .variety-banner { position: absolute; left: 30px; top: 344px; width: 452px; height: 74px; }
  .variety-name {
    position: absolute; left: 30px; top: 344px; width: 452px; height: 74px;
    display: flex; align-items: center; justify-content: center;
    font-family: "Alfa Slab One", serif; font-size: 28px; letter-spacing: 3px;
    color: var(--copper-deep);
  }

  .origin {
    position: absolute; left: 0; right: 0; top: 428px;
    text-align: center;
    font-family: "IM Fell English SC", serif; font-size: 11.5px; letter-spacing: 1.2px;
    color: var(--ink);
  }
  .volume {
    position: absolute; left: 0; right: 0; top: 448px;
    display: flex; justify-content: center; align-items: baseline; gap: 10px;
    color: var(--copper);
  }
  .volume .stars { font-size: 11px; letter-spacing: 3px; }
  .volume .amount { font-family: "IM Fell English", serif; font-style: italic; font-size: 24px; }
  .volume .amount small { font-size: 11px; font-style: normal; }
</style>
</head>
<body>
<main class="board">

  <article class="label label--rounded">
    <h1 class="brand-title">Marden Hollow</h1>
    <p class="brand-sub"><span class="star">★</span>STILL WORKS<span class="star">★</span></p>
    <div class="scene" role="img" aria-label="Engraved illustration of Elias Thornbury on horseback leading mounted colonial officers"></div>
    <div class="maker-mark"><span class="dot"></span><span class="name">Marden Hollow<br>Still Works</span></div>
    <svg class="variety-banner" viewBox="0 0 452 74" aria-hidden="true">
      <rect x="22" y="4" width="408" height="66" fill="none" stroke="var(--copper)" stroke-width="3"/>
      <rect x="28" y="9" width="396" height="56" fill="none" stroke="var(--copper)" stroke-width="1"/>
      <rect x="40" y="14" width="372" height="46" rx="23" fill="var(--paper)" stroke="var(--copper)" stroke-width="3"/>
      <circle cx="18" cy="37" r="17" fill="none" stroke="var(--copper)" stroke-width="3"/>
      <circle cx="434" cy="37" r="17" fill="none" stroke="var(--copper)" stroke-width="3"/>
      <path d="M216 70 L226 78 L236 70" fill="var(--copper)"/>
    </svg>
    <p class="variety-name">WHITE WHISKEY</p>
    <p class="origin">Distilled &amp; Bottled in Marden Hollow, Pennsylvania</p>
    <p class="volume"><span class="stars">★★★★★★★★★★★★</span><span class="amount">750 <small>ML</small></span><span class="stars">★★★★★★★★★★★★</span></p>
  </article>

  <article class="label label--deckle">
    <h1 class="brand-title">Marden Hollow</h1>
    <p class="brand-sub"><span class="star">★</span>STILL WORKS<span class="star">★</span></p>
    <div class="scene" role="img" aria-label="Engraved illustration of Elias Thornbury on horseback leading mounted colonial officers"></div>
    <div class="maker-mark"><span class="dot"></span><span class="name">Marden Hollow<br>Still Works</span></div>
    <svg class="variety-banner" viewBox="0 0 452 74" aria-hidden="true">
      <rect x="22" y="4" width="408" height="66" fill="none" stroke="var(--copper)" stroke-width="3"/>
      <rect x="28" y="9" width="396" height="56" fill="none" stroke="var(--copper)" stroke-width="1"/>
      <rect x="40" y="14" width="372" height="46" rx="23" fill="var(--paper)" stroke="var(--copper)" stroke-width="3"/>
      <circle cx="18" cy="37" r="17" fill="none" stroke="var(--copper)" stroke-width="3"/>
      <circle cx="434" cy="37" r="17" fill="none" stroke="var(--copper)" stroke-width="3"/>
      <path d="M216 70 L226 78 L236 70" fill="var(--copper)"/>
    </svg>
    <p class="variety-name">WHITE WHISKEY</p>
    <p class="origin">Distilled &amp; Bottled in Marden Hollow, Pennsylvania</p>
    <p class="volume"><span class="stars">★★★★★★★★★★★★</span><span class="amount">750 <small>ML</small></span><span class="stars">★★★★★★★★★★★★</span></p>
  </article>

</main>
</body>
</html>
```